Come Play With Us!!! We are the Elite

We need a hiring flyer to hand out to potential recruits.
Please promote our social pages.
Something attractive, and informative with calls to action to contact us.
Please promote for people to follow us on social media.
We would like to list the following advantages to work here:
• Industry Leading Compensation
• Structured Career Advancement
• Safe Work Environment
• Work Promise Policy (Full Time Staff)
• Health & Dental Benefits
• Paid Training Programs
• Paid Clothing Allowance
• Paid Boot Allowance
• Positive Culture
• Progressive Culture
• Equal Opportunity Employer
• Veteran Friendly Employer
• New Equipment
• Paid Leadership Training
• Transparent Communication
• Community Focused
• Prestigious Clientele
• Local Work
• Focused on using industry leading tech
• Tool Purchase Program
• Family Atmosphere
• Team Events (Sports games, Lunches, Get togethers, Etc)
• Work Life balance
• Daily On Call Snow Pay
- Sick Pay
- Positive reputation
• Bonus’s available:
o Winter Shift Premium
o Referral Bonus
o Project Incentives
Current Positions open:
- Winter Crew Members
- Salt Truck Driver/Operator (AZ/DZ/AR)
- Winter Equipment Operators
- Construction Foreperson
Landscape and Construction

```html
<!DOCTYPE html>
<html lang="en">
<head>
<meta charset="utf-8">
<title>Hiring Flyer – Winter Crew</title>
<link href="https://fonts.googleapis.com/css2?family=Archivo:wght@700;800&family=Oswald:wght@500;600&family=Saira+Semi+Condensed:wght@600;700&display=swap" rel="stylesheet">
<style>
  :root{
    --paper:#e6e7e8;
    --ink:#333335;
    --teal:#14a99c;
    --green:#44bb7e;
    --green-dark:#3aaa70;
    --slate:#555557;
    --white:#ffffff;
  }
  *{margin:0;padding:0;box-sizing:border-box}
  html,body{width:849px;height:1200px;overflow:hidden;background:var(--paper)}
  .flyer{position:relative;width:849px;height:1200px;background:var(--paper);overflow:hidden}
  .layer{position:absolute;left:0;top:0}
  .greeting{position:absolute;left:40px;top:52px;color:var(--ink);font-family:"Archivo",Arial,sans-serif;font-weight:700}
  .greeting .hello{display:block;color:var(--teal);font-weight:800;font-size:121px;line-height:104px;letter-spacing:-1px}
  .greeting .line{display:block;font-size:61px;line-height:64px;letter-spacing:0.5px}

  .positions{position:absolute;left:34px;top:336px;color:var(--white);font-family:"Oswald","Arial Narrow",sans-serif}
  .positions h2{font-weight:600;font-size:46px;line-height:56px;height:56px;letter-spacing:-0.5px;transform:scaleX(.9);transform-origin:left;white-space:nowrap}
  .positions ul{list-style:none;margin-top:-2px}
  .positions li{position:relative;display:block;height:44.7px;line-height:44.7px;padding-left:12px;font-weight:500;font-size:31px;letter-spacing:-1px;white-space:nowrap;transform:scaleX(.88);transform-origin:left}
  .positions li::before{content:"";position:absolute;left:0;top:50%;width:5px;height:5px;margin-top:-1px;background:var(--white)}

  .advantages-title{position:absolute;left:26px;top:584px;color:var(--white);font-family:"Oswald","Arial Narrow",sans-serif;font-weight:600;font-size:43px;line-height:48px;letter-spacing:-0.5px;white-space:nowrap;transform:scaleX(.86);transform-origin:left}

  .perks{position:absolute;top:632px;height:438px;background:var(--slate);list-style:none;color:var(--white);font-family:"Saira Semi Condensed","Arial Narrow",sans-serif;font-weight:700;font-size:17px;letter-spacing:.6px}
  .perks li{position:relative;display:block;height:26.7px;line-height:26.7px;padding-left:10px;white-space:nowrap}
  .perks li::before{content:"";position:absolute;left:0;top:50%;width:3.5px;height:3.5px;margin-top:-1px;background:var(--white)}
  .perks-left{left:0;width:417px;padding:5px 0 0 35px}
  .perks-right{left:432px;width:417px;padding:5px 0 0 13px}
  .perks .note{font-size:14.5px;padding-left:12px}
  .perks .note::before{display:none}

  .divider{position:absolute;left:0;top:1073px;width:849px;height:4px;background:var(--slate)}
  .footer{position:absolute;left:0;top:1078px;width:849px;height:122px;background:var(--teal)}
  .follow{position:absolute;left:118px;top:8px;color:var(--white);font-family:"Oswald","Arial Narrow",sans-serif;font-weight:600;font-style:italic;white-space:nowrap;transform:skewX(-6deg) rotate(-4deg)}
  .follow .w1{display:inline-block;font-size:54px;transform:scaleX(.8);transform-origin:left;margin-right:-30px}
  .follow .w2{display:inline-block;font-size:68px;transform:scaleX(.8) translateY(8px);transform-origin:left}
  .social{position:absolute;left:0;top:0}
  .social text{font-family:"Saira Semi Condensed","Arial Narrow",sans-serif;font-weight:700;font-size:11px;fill:var(--white)}
</style>
</head>
<body>
<main class="flyer">
  <svg class="layer" width="849" height="640" viewBox="0 0 849 640">
    <defs>
      <linearGradient id="photoTone" x1="0" y1="0" x2="1" y2="1">
        <stop offset="0" stop-color="#f4f4f2"/>
        <stop offset=".45" stop-color="#d9c2ad"/>
        <stop offset=".7" stop-color="#8b8a8c"/>
        <stop offset="1" stop-color="#4a4a4e"/>
      </linearGradient>
      <linearGradient id="greenBand" x1="0" y1="0" x2="1" y2="0">
        <stop offset="0" stop-color="#3aaa70"/>
        <stop offset="1" stop-color="#44bb7e"/>
      </linearGradient>
    </defs>
    <polygon points="609,0 849,0 849,540 264,540 264,327" fill="url(#photoTone)" role="img" aria-label="Photo of a business handshake in a bright office"/>
    <rect x="0" y="540" width="849" height="34" fill="var(--slate)"/>
    <polygon points="0,327 489,327 651,574 0,574" fill="url(#greenBand)"/>
    <polygon points="0,581 450,581 484,628 0,628" fill="var(--teal)"/>
    <rect x="0" y="628" width="849" height="4" fill="var(--teal)"/>
  </svg>

  <h1 class="greeting">
    <span class="hello">HELLO</span>
    <span class="line">POTENTIAL</span>
    <span class="line">RECRUITS</span>
  </h1>

  <section class="positions">
    <h2>CURRENT POSITIONS OPEN</h2>
    <ul>
      <li>Winter Crew Members</li>
      <li>Salt Truck Driver/Operator (AZ/DZ/AR)</li>
      <li>Winter Equipment Operators</li>
      <li>Construction Foreperson</li>
    </ul>
  </section>

  <h2 class="advantages-title">ADVANTAGES TO WORK HERE</h2>

  <ul class="perks perks-left">
    <li>Industry Leading Compensation</li>
    <li>Structured Career Advancement</li>
    <li>Safe Work Environment</li>
    <li>Work Promise Policy (Full Time Staff)</li>
    <li>Health &amp; Dental Benefits</li>
    <li>Paid Training Programs</li>
    <li>Paid Clothing Allowance</li>
    <li>Paid Boot Allowance</li>
    <li>Positive Culture</li>
    <li>Progressive Culture</li>
    <li>Equal Opportunity Employer</li>
    <li>Veteran Friendly Employer</li>
    <li>New Equipment</li>
    <li>Paid Leadership Training</li>
    <li>Transparent Communication</li>
    <li>Community Focused</li>
  </ul>
  <ul class="perks perks-right">
    <li>Prestigious Clientele</li>
    <li>Local Work</li>
    <li>Focused on using industry leading tech</li>
    <li>Tool Purchase Program</li>
    <li>Family Atmosphere</li>
    <li>Team Events</li>
    <li class="note">(Sports games, Lunches, Get togethers, Etc)</li>
    <li>Work Life balance</li>
    <li>Daily On Call Snow Pay</li>
    <li>Sick Pay</li>
    <li>Positive reputation</li>
    <li>Bonus’s available:</li>
    <li>Winter Shift Premium</li>
    <li>Referral Bonus</li>
    <li>Project Incentives</li>
  </ul>

  <div class="divider"></div>

  <footer class="footer">
    <p class="follow"><span class="w1">FOLLOW</span> <span class="w2">US!</span></p>
    <svg class="social" width="849" height="122" viewBox="0 0 849 122" aria-label="Social media pages">
      <g fill="none" stroke="var(--white)" stroke-width="3">
        <circle cx="409" cy="43" r="27"/>
        <circle cx="481" cy="43" r="27"/>
        <circle cx="555" cy="43" r="27"/>
        <circle cx="627" cy="43" r="27"/>
        <circle cx="700" cy="43" r="27"/>
      </g>
      <g text-anchor="middle">
        <text x="409" y="47">PAGE</text>
        <text x="481" y="47">NEWS</text>
        <text x="555" y="47">PHOTO</text>
        <text x="627" y="47">IDEAS</text>
        <text x="700" y="47">MORE</text>
      </g>
    </svg>
  </footer>
</main>
</body>
</html>
```